Design Executive Business Acquisitons Brokerage Website

Modern but Professional with the colours black, purple and white. Must convey authenticity, and progressive out-of-square thinking. We are a boutique Business Broking firm located in Brisbane QLD Australia. We market and sell businesses with sales revenue/turnover from Au $1M to $15 M + or have a minimum staff of 15 to 50 staff. Our buyers are generally acquisitions corporate buyers. We need a modern approach but conservative tones. We are serious and experienced. We say it as it is and we get the job done! We sell in the following industries but not limited to, engineering, manufacturing, agriculture, recruitment, transportation, warehousing, services, IT,eCommerce, civil construction,mining, wholesaling, dealerships, MEdical (all), service stations, Management rights, high-end retail, building construction,importing,exporting to name a few.

Target Market(s)

SME Corporate Public & Private exsisting large businesses that are looking to buy through acquisitions

Industry/Entity Type

Coommercial executive Business Sale

Number of Pages Required

5+ page

Font styles to use
Sans Serif

Requirements
Must have
• Serious tones, searchar, NDA form, serious corporate executive feel. Include all corporaate colors,black less whit purples.Corporate Logo
Nice to have
• carosel moving right to left of industry pictures as per above and attached industries
Should not have
• No hand shaking, business people.

```html
<!DOCTYPE html>
<html lang="en">
<head>
<meta charset="utf-8">
<title>Northgate Acquisitions Group</title>
<link href="https://fonts.googleapis.com/css2?family=Roboto:wght@400;500;700;900&display=swap" rel="stylesheet">
<style>
:root{
  --purple:#5b3f8c;
  --purple-deep:#4a2f78;
  --ink:#111111;
  --text:#444444;
  --muted:#666666;
  --white:#ffffff;
  --mist:#f4f4f8;
  --lavender:#eef0f7;
  --footer:#0d0d0d;
  --f1:#c9a7e6;
  --f2:#9a8ad8;
  --f3:#7a72c0;
  --f4:#5f7a72;
  --line:#dddddd;
}
*{box-sizing:border-box;margin:0;padding:0}
html,body{width:1200px;height:4066px;overflow:hidden}
body{font-family:'Roboto',Arial,sans-serif;color:var(--ink);background:var(--white);position:relative}
.abs{position:absolute}
.btn{position:absolute;display:flex;align-items:center;justify-content:center;background:var(--purple);color:var(--white);font-weight:700;font-size:15px;border-radius:24px;text-transform:uppercase;letter-spacing:.2px}
.section-title{position:absolute;left:0;width:1200px;text-align:center;font-weight:700;font-size:38px;text-transform:uppercase;color:var(--ink)}

/* hero */
.hero{position:absolute;left:0;top:0;width:1200px;height:628px;background:linear-gradient(100deg,#3a3d44 0%,#6c727c 35%,#9aa0a8 60%,#c8ccd2 100%);overflow:hidden}
.brand{position:absolute;display:flex;align-items:center;gap:10px;font-weight:700;font-size:30px;color:var(--white)}
.brand .dot{width:40px;height:40px;border-radius:50%;background:var(--white)}
.brand small{display:block;font-size:11px;font-weight:500;letter-spacing:1.2px;margin-top:-2px}
.nav{position:absolute;top:30px;left:551px;display:flex;gap:40px;font-size:15px;font-weight:500;color:var(--white)}
.nav .active{border-bottom:2px solid var(--white);padding-bottom:4px}
.hero h1{position:absolute;left:110px;top:205px;font-size:97px;font-weight:900;color:var(--white);line-height:1}
.hero h2{position:absolute;left:112px;top:303px;font-size:44px;font-weight:700;color:var(--white);line-height:1}
.hero p{position:absolute;left:112px;top:365px;width:460px;font-size:14.5px;line-height:25px;color:var(--white);font-weight:500}
.dots{position:absolute;left:124px;top:498px;display:flex;gap:7px}
.dots span{width:13px;height:13px;border-radius:50%;border:2px solid var(--white)}
.dots span:first-child{background:var(--white)}

/* about */
.vlabel{position:absolute;left:108px;top:752px;transform:rotate(-90deg) translateX(-100%);transform-origin:0 0;font-size:13px;font-weight:500;color:var(--purple);letter-spacing:.5px}
.vline{position:absolute;left:122px;top:830px;width:2px;height:72px;background:var(--purple)}
.about-title{position:absolute;left:144px;top:740px;font-size:38px;font-weight:700}
.about-copy{position:absolute;left:144px;width:420px;font-size:13.5px;line-height:25.5px;color:var(--text);text-align:justify}

/* brands */
.divider{position:absolute;left:112px;top:1186px;width:976px;height:1px;background:var(--line)}
.partner{position:absolute;top:1311px;height:28px;border-radius:4px;background:#c7c9cd}

/* services */
.services{position:absolute;left:0;top:1437px;width:1200px;height:687px;background:var(--mist);overflow:hidden}
.card-title{position:absolute;width:311px;text-align:center;font-size:21px;font-weight:500;color:var(--ink)}
.card-text{position:absolute;width:311px;text-align:center;font-size:13.5px;line-height:26px;color:var(--text);padding:0 6px}

/* funnel */
.step-title{position:absolute;font-size:19px;font-weight:500;color:#222}
.step-text{position:absolute;width:420px;font-size:13px;line-height:19px;color:var(--muted)}

/* buyers */
.buyers{position:absolute;left:0;top:2615px;width:1200px;height:453px;background:var(--lavender);overflow:hidden}
.buyers h3{position:absolute;left:112px;top:95px;font-size:52px;font-weight:700;color:var(--ink)}
.buyers h4{position:absolute;left:112px;top:160px;font-size:34px;font-weight:500;line-height:47px;color:var(--ink);text-transform:uppercase}
.buyers p{position:absolute;left:112px;top:268px;width:420px;font-size:12.5px;line-height:25.5px;color:var(--text)}

/* blog */
.post{position:absolute;top:3221px;width:305px;height:420px;background:var(--white);box-shadow:0 2px 10px rgba(0,0,0,.12)}
.post .date{position:absolute;left:81px;top:202px;width:142px;height:36px;border-radius:18px;background:var(--purple);color:var(--white);font-size:13px;font-weight:700;display:flex;align-items:center;justify-content:center}
.post h5{position:absolute;left:23px;top:270px;width:260px;font-size:19px;font-weight:500;line-height:26px;color:var(--ink)}
.post p{position:absolute;left:18px;top:336px;width:270px;font-size:12.5px;line-height:24px;color:var(--muted)}
.post .more{position:absolute;left:20px;top:386px;display:flex;align-items:center;gap:12px;font-size:14px;font-weight:500;color:var(--purple)}
.post .more::before{content:"";width:40px;height:2px;background:var(--purple)}

/* footer */
.footer{position:absolute;left:0;top:3730px;width:1200px;height:336px;background:var(--footer);color:var(--white)}
.footer h6{position:absolute;top:80px;font-size:15px;font-weight:700}
.field{position:absolute;height:35px;border:1px solid #cfcfcf;background:var(--footer);color:#bbb;font-size:12px;padding:0 10px;display:flex;align-items:center}
.links{position:absolute;left:493px;top:107px;font-size:12.5px;line-height:26.4px}
.contact{position:absolute;left:654px;top:107px;font-size:12.5px;line-height:26.4px}
.contact div{display:flex;align-items:center;gap:8px}
.social{position:absolute;top:3876px;width:32px;height:32px;border-radius:50%;background:#1e63c4}
.copy{position:absolute;left:0;top:4023px;width:1200px;text-align:center;font-size:13px;color:var(--white)}
</style>
</head>
<body>

<header class="hero">
  <div role="img" aria-label="Photo of an office meeting with colleagues reviewing a tablet" class="abs" style="left:0;top:0;width:1200px;height:628px;background:linear-gradient(90deg,rgba(40,42,48,.55) 0%,rgba(40,42,48,.2) 50%,rgba(0,0,0,0) 100%)"></div>
  <div class="brand" style="left:112px;top:12px"><span class="dot"></span><div>northgate<small>ACQUISITIONS GROUP</small></div></div>
  <nav class="nav"><span class="active">HOME</span><span>ABOUT US</span><span>OUR SERVICES</span><span>BLOG</span><span>CONTACT US</span></nav>
  <h1>NORTHGATE</h1>
  <h2>ACQUISITIONS GROUP</h2>
  <p>Lorem ipsum dolor sit amet, consectetur adipiscing elit, sed do eiusmod tempor incididunt ut labore et dolore magna aliqua.</p>
  <div class="btn" style="left:112px;top:431px;width:153px;height:40px">Get Started</div>
  <div class="dots"><span></span><span></span><span></span><span></span></div>
  <svg class="abs" style="left:555px;top:600px" width="90" height="28" viewBox="0 0 90 28"><polygon points="0,28 45,0 90,28" fill="#fff"/><polyline points="38,14 45,20 52,14" fill="none" stroke="#333" stroke-width="1.6"/></svg>
</header>

<section>
  <div class="vlabel">ABOUT US</div>
  <div class="vline"></div>
  <h2 class="about-title">WHO WE ARE</h2>
  <p class="about-copy" style="top:800px">Lorem ipsum dolor sit amet, consectetur adipiscing elit, sed do eiusmod tempor incididunt ut labore et dolore magna aliqua. Quis isuspendisse ultrices gravida. Risus commodo viverra maecenas accumsan lacus vel facilisis.</p>
  <p class="about-copy" style="top:917px">Lorem ipsum dolor sit amet, consectetur adipiscing elit, sed do eiusmod tempor incididunt ut labore et dolore magna aliqua. Quis isuspendisse ultrices gravida.</p>
  <div class="btn" style="left:144px;top:1018px;width:154px;height:43px">Learn More</div>
  <div role="img" aria-label="Photo of an office workspace" class="abs" style="left:720px;top:710px;width:362px;height:332px;background:linear-gradient(135deg,#9a9ea4,#d9dbde)"></div>
  <div class="abs" style="left:679px;top:753px;width:355px;height:346px;border:4px solid var(--purple)"></div>
  <div role="img" aria-label="Photo of a team meeting around a conference table" class="abs" style="left:646px;top:785px;width:358px;height:287px;background:linear-gradient(135deg,#7d8794,#b9c0c8 55%,#e4e6e9)"></div>
</section>

<section>
  <div class="divider"></div>
  <h2 class="section-title" style="top:1214px">Brand Awareness</h2>
  <svg class="abs" style="left:110px;top:1315px" width="14" height="22"><polyline points="11,2 3,11 11,20" fill="none" stroke="#777" stroke-width="2"/></svg>
  <div class="partner" style="left:145px;width:135px"></div>
  <div class="partner" style="left:365px;width:125px"></div>
  <div class="partner" style="left:575px;width:122px"></div>
  <div class="partner" style="left:784px;width:96px"></div>
  <div class="partner" style="left:963px;width:93px"></div>
  <svg class="abs" style="left:1076px;top:1315px" width="14" height="22"><polyline points="3,2 11,11 3,20" fill="none" stroke="#777" stroke-width="2"/></svg>
</section>

<section class="services">
  <h2 class="section-title" style="top:83px">Our Services</h2>
  <div role="img" aria-label="Photo of a man thinking in front of a laptop" class="abs" style="left:112px;top:158px;width:311px;height:219px;background:linear-gradient(135deg,#2d3550,#55607c 60%,#8893aa)"></div>
  <div role="img" aria-label="Overhead photo of a team working around a table" class="abs" style="left:444px;top:158px;width:311px;height:219px;background:linear-gradient(135deg,#8c97a3,#c3cad1 55%,#9aa4ad)"></div>
  <div role="img" aria-label="Photo of a presentation at a whiteboard" class="abs" style="left:777px;top:158px;width:311px;height:219px;background:linear-gradient(135deg,#5f6670,#a9afb6 55%,#d6d9dc)"></div>
  <div class="card-title" style="left:112px;top:393px">The standard Lorem</div>
  <div class="card-title" style="left:444px;top:393px">The standard Lorem</div>
  <div class="card-title" style="left:777px;top:393px">The standard Lorem</div>
  <p class="card-text" style="left:112px;top:423px">Lorem ipsum dolt, consectetur adipiscing elit, sed mod tempor incididunt ut labore et dolore magna aliua. Ut enim ad minim veniam, quis nos</p>
  <p class="card-text" style="left:444px;top:423px">Lorem ipsum dolt, consectetur adipiscing elit, sed mod tempor incididunt ut labore et dolore magna aliua. Ut enim ad minim veniam, quis nos</p>
  <p class="card-text" style="left:777px;top:423px">Lorem ipsum dolt, consectetur adipiscing elit, sed mod tempor incididunt ut labore et dolore magna aliua. Ut enim ad minim veniam, quis nos</p>
  <div class="btn" style="left:181px;top:549px;width:174px;height:45px">Learn More</div>
  <div class="btn" style="left:513px;top:549px;width:174px;height:45px;background:#3c3c3c">Learn More</div>
  <div class="btn" style="left:846px;top:549px;width:174px;height:45px">Learn More</div>
</section>

<section>
  <svg class="abs" style="left:0;top:2190px" width="1200" height="340" viewBox="0 2190 1200 340">
    <defs><linearGradient id="band" x1="0" x2="1"><stop offset="0" stop-color="#bdbdbd"/><stop offset="1" stop-color="#f2f2f2"/></linearGradient></defs>
    <polygon points="167,2263 515,2263 459,2293 167,2293" fill="url(#band)"/>
    <polygon points="223,2342 459,2342 404,2373 223,2373" fill="url(#band)"/>
    <polygon points="278,2421 404,2421 351,2452 278,2452" fill="url(#band)"/>
    <polygon points="114,2215 515,2215 486,2263 143,2263" fill="var(--f1)"/>
    <polygon points="167,2293 459,2293 434,2342 193,2342" fill="var(--f2)"/>
    <polygon points="223,2373 404,2373 385,2421 243,2421" fill="var(--f3)"/>
    <polygon points="278,2452 351,2452 314,2507" fill="var(--f4)"/>
    <g fill="#fff" font-family="Roboto, sans-serif" font-size="21" text-anchor="middle">
      <text x="313" y="2247">01</text><text x="313" y="2325">02</text><text x="315" y="2405">03</text><text x="314" y="2480">04</text>
    </g>
    <g stroke="#999" stroke-width="1.2">
      <line x1="516" y1="2242" x2="679" y2="2242"/><line x1="461" y1="2323" x2="625" y2="2323"/>
      <line x1="407" y1="2402" x2="570" y2="2402"/><line x1="351" y1="2485" x2="513" y2="2485"/>
    </g>
    <g fill="none" stroke-width="2">
      <circle cx="602" cy="2218" r="10" stroke="var(--f1)"/><line x1="602" y1="2218" x2="602" y2="2212" stroke="var(--f1)"/>
      <circle cx="548" cy="2294" r="11" stroke="var(--f2)"/><circle cx="548" cy="2294" r="4" stroke="var(--f2)"/>
      <circle cx="494" cy="2378" r="9" stroke="var(--f3)"/><circle cx="494" cy="2378" r="3" stroke="var(--f3)"/>
      <path d="M428 2455 h16 v6 a8 8 0 0 1 -16 0 z M436 2469 v6 M430 2476 h12" stroke="var(--f4)"/>
    </g>
  </svg>
  <div class="step-title" style="left:709px;top:2210px">FINIBUS BONORUM ET</div>
  <p class="step-text" style="left:709px;top:2239px">Sed ut perspiciatis unde omnis iste natus sit voluptatem accusantium doloremque laudantium, totam</p>
  <div class="step-title" style="left:654px;top:2296px">FINIBUS BONORUM ET</div>
  <p class="step-text" style="left:654px;top:2325px">Sed ut perspiciatis unde omnis iste natus sit voluptatem accusantium doloremque laudantium, totam</p>
  <div class="step-title" style="left:597px;top:2383px">FINIBUS BONORUM ET</div>
  <p class="step-text" style="left:597px;top:2412px">Sed ut perspiciatis unde omnis iste natus sit voluptatem accusantium doloremque laudantium, totam</p>
  <div class="step-title" style="left:542px;top:2469px">FINIBUS BONORUM ET</div>
  <p class="step-text" style="left:542px;top:2498px">Sed ut perspiciatis unde omnis iste natus sit voluptatem accusantium doloremque laudantium, totam</p>
</section>

<section class="buyers">
  <div role="img" aria-label="Photo of a thoughtful man in glasses working at a laptop" class="abs" style="left:537px;top:0;width:663px;height:453px;background:linear-gradient(90deg,rgba(238,240,247,1) 0%,rgba(200,205,215,.6) 35%,#a9b0bc 70%,#d7dbe2 100%)"></div>
  <h3>AU $1M TO $15 M +.</h3>
  <h4>Our buyers are generally<br>acquisition buyers</h4>
  <p>Lorem ipsum dolor sit amet, consectetur adipiscing elit, sed do eiusmod tempor incididunt ut labore et dolore magna aliqua. Quis isuspendisse ultrices gravida. Risus commodo viverra maecenas accumsan lacus vel facilisis.</p>
</section>

<section>
  <h2 class="section-title" style="top:3145px">Latest Blog</h2>
  <article class="post" style="left:112px">
    <div role="img" aria-label="Photo of a woman writing notes beside a laptop" class="abs" style="left:0;top:0;width:305px;height:220px;background:linear-gradient(135deg,#6b5a47,#b39a78 55%,#ddd3c4)"></div>
    <div class="date">MAY 21, 2022</div>
    <h5>The standard Lorem Ipsum passage, use the 1500s</h5>
    <p>Lorem ipsum dolor sit amet, teturipiscing elit, sed do eiusd tempor</p>
    <div class="more">READ MORE</div>
  </article>
  <article class="post" style="left:448px">
    <div role="img" aria-label="Photo of hands working on paperwork with a calculator" class="abs" style="left:0;top:0;width:305px;height:220px;background:linear-gradient(135deg,#cbb79c,#ece3d6 55%,#bfb3a4)"></div>
    <div class="date">MAR 2, 2022</div>
    <h5>The standard Lorem Ipsum passage, use the 1500s</h5>
    <p>Lorem ipsum dolor sit amet, teturipiscing elit, sed do eiusd tempor</p>
    <div class="more">READ MORE</div>
  </article>
  <article class="post" style="left:785px">
    <div role="img" aria-label="Photo of a workshop team reviewing a laptop" class="abs" style="left:0;top:0;width:303px;height:220px;background:linear-gradient(135deg,#5a6470,#9aa3ad 50%,#b5533f)"></div>
    <div class="date">JAN 4, 2022</div>
    <h5>The standard Lorem Ipsum passage, use the 1500s</h5>
    <p>Lorem ipsum dolor sit amet, teturipiscing elit, sed do eiusd tempor</p>
    <div class="more">READ MORE</div>
  </article>
</section>

<footer class="footer">
  <h6 style="left:112px">GET INSIGHTS &amp; UPDATES</h6>
  <div class="field" style="left:112px;top:107px;width:158px">Name</div>
  <div class="field" style="left:279px;top:107px;width:160px">Phone</div>
  <div class="field" style="left:112px;top:154px;width:327px">Enter Email</div>
  <div class="abs" style="left:112px;top:200px;width:327px;height:38px;background:var(--purple);display:flex;align-items:center;justify-content:center;font-size:14px;font-weight:700">SUBSCRIBE</div>
  <h6 style="left:493px">QUICK LINKS</h6>
  <div class="links">Home<br>About Us<br>Our Services<br>Blog<br>Contact Us</div>
  <h6 style="left:654px">CONTACT INFO</h6>
  <div class="contact">
    <div><svg width="10" height="13" viewBox="0 0 10 13"><path d="M5 0a5 5 0 0 1 5 5c0 3.5-5 8-5 8S0 8.5 0 5a5 5 0 0 1 5-5z" fill="#fff"/><circle cx="5" cy="5" r="2" fill="#0d0d0d"/></svg>123 Avenue name, City name</div>
    <div style="padding-left:18px">10150, United States</div>
    <div><svg width="11" height="11" viewBox="0 0 11 11"><path d="M2 0l2 3-1 1.5c.8 1.5 2 2.7 3.5 3.5L8 7l3 2-1 2C5 11 0 6 0 1z" fill="#fff"/></svg>07 3100 2400</div>
    <div><svg width="12" height="9" viewBox="0 0 12 9"><rect x=".5" y=".5" width="11" height="8" fill="none" stroke="#fff"/><polyline points=".5,.5 6,5 11.5,.5" fill="none" stroke="#fff"/></svg>info@northgateacquisitions.com</div>
  </div>
  <div class="brand" style="left:920px;top:84px;font-size:26px;gap:8px"><span class="dot" style="width:34px;height:34px"></span><div>northgate<small style="font-size:9px">ACQUISITIONS GROUP</small></div></div>
  <div class="abs" style="left:103px;top:276px;width:994px;height:1px;background:#444"></div>
</footer>
<div class="social" style="left:925px;background:#3b5998"></div>
<div class="social" style="left:969px;background:#c13584"></div>
<div class="social" style="left:1012px;background:#0e76a8"></div>
<div class="social" style="left:1056px;background:#1e63c4"></div>
<div class="copy">© 2022 NORTHGATE ACQUISITIONS GROUP. All Rights Reserved.</div>

</body>
</html>
```